Company Letter head for real estate company

need company letter head
Updates

You can use the logo that I submitted. no need to create a new one

Requirements
Must have
• must have my address on it..38264 WINDMERE, HARLOW, OH 48302-1175, INFO@MUVRO.CA

```html
<!DOCTYPE html>
<html lang="en">
<head>
<meta charset="utf-8">
<title>Muvro Letterhead</title>
<link href="https://fonts.googleapis.com/css2?family=Lato:wght@300;400;700&display=swap" rel="stylesheet">
<style>
  :root {
    --stage: #6a9fa0;
    --paper: #ffffff;
    --green: #7dbd3a;
    --charcoal: #3a3a3a;
    --ink: #333333;
    --muted: #555555;
  }
  * { box-sizing: border-box; margin: 0; padding: 0; }
  html, body { width: 1200px; height: 800px; overflow: hidden; }
  body {
    background: var(--stage);
    font-family: "Lato", Arial, sans-serif;
    display: flex; align-items: center; justify-content: center;
  }
  .letterhead {
    position: relative;
    width: 540px; height: 764px;
    background: var(--paper);
    box-shadow: 0 10px 30px rgba(0,0,0,.2);
    overflow: hidden;
  }
  .header-wave, .footer-bands { position: absolute; left: 0; width: 100%; display: block; }
  .header-wave { top: 0; height: 190px; }
  .footer-bands { bottom: 0; height: 60px; }
  .contact {
    position: absolute; top: 62px; right: 28px;
    color: #fff; font-size: 8.5px; font-weight: 400;
    line-height: 1.6; letter-spacing: .3px; text-align: left;
  }
  .contact li { list-style: none; display: flex; align-items: center; gap: 5px; }
  .contact svg { width: 8px; height: 8px; }
  .brand {
    position: absolute; top: 52px; left: 46px;
    display: flex; align-items: center; gap: 8px;
    font-size: 24px; font-weight: 700; color: var(--charcoal); letter-spacing: 2px;
  }
  .brand-mark { width: 14px; height: 14px; background: var(--green); }
  .letter {
    position: absolute; top: 165px; left: 46px; right: 46px;
    color: var(--ink); font-size: 9.5px; line-height: 1.35;
  }
  .letter-date { margin-bottom: 12px; }
  .recipient { margin-bottom: 12px; }
  .salutation { font-weight: 700; font-size: 11px; margin-bottom: 10px; }
  .letter p.body { margin-bottom: 10px; }
  .signoff { margin-top: 14px; color: var(--muted); }
  .signature {
    margin-top: 10px; width: 150px; height: 30px;
    background: linear-gradient(90deg, #e9e9e9, #f6f6f6);
  }
</style>
</head>
<body>
  <main class="letterhead">
    <svg class="header-wave" viewBox="0 0 540 190" preserveAspectRatio="none" aria-hidden="true">
      <path d="M40 0 H540 V150 C470 182 390 170 320 120 C250 68 170 20 40 0 Z" fill="var(--charcoal)"/>
      <path d="M70 0 H540 V140 C470 172 395 160 328 112 C260 62 190 18 70 0 Z" fill="var(--green)"/>
      <path d="M40 0 C170 20 250 68 320 120 C390 170 470 182 540 150" fill="none" stroke="#fff" stroke-width="2"/>
    </svg>
    <ul class="contact">
      <li>38264 WINDMERE,</li>
      <li>HARLOW, OH</li>
      <li><svg viewBox="0 0 10 10"><path d="M2 1 L4 1 L5 3 L4 4 Q5 6 6 6 L7 5 L9 6 L9 8 Q5 9 1 3 Z" fill="#fff"/></svg>48302-1175</li>
      <li><svg viewBox="0 0 10 10"><rect x="1" y="2" width="8" height="6" fill="#fff"/><path d="M1 2 L5 5 L9 2" stroke="var(--green)" fill="none"/></svg>INFO@MUVRO.CA</li>
    </ul>
    <div class="brand"><span class="brand-mark"></span>MUVRO</div>
    <article class="letter">
      <p class="letter-date">January-03-2020</p>
      <p class="recipient">Mr. Peter Lane<br>President</p>
      <p class="recipient">Arcline Corporation<br>210 Harbor Row, Suite# 4<br>City, State, 120023</p>
      <p class="salutation">Dear Mr. Peter</p>
      <p class="body">Lorem ipsum dolor sit amet, consectetur adipisicing elit, sed do eiusmod tempor incididunt ut labore et dolore magna aliqua. Ut enim ad minim veniam, quis nostrud exercitation ullamco laboris nisi ut aliquip ex ea commodo consequat. Duis aute irure dolor in reprehenderit in voluptate velit esse cillum dolore eu fugiat nulla pariatur.</p>
      <p class="body">Lorem ipsum dolor sit amet, consectetur adipisicing elit, sed do eiusmod tempor incididunt ut labore et dolore magna aliqua. Ut enim ad minim veniam, quis nostrud exercitation ullamco laboris nisi ut aliquip ex ea commodo consequat. Duis aute irure dolor in reprehenderit in voluptate velit esse cillum dolore eu fugiat nulla pariatur.</p>
      <p class="body">Lorem ipsum dolor sit amet, consectetur adipisicing elit, sed do eiusmod tempor incididunt ut labore et dolore magna aliqua. Ut enim ad minim veniam, quis nostrud exercitation ullamco laboris nisi ut aliquip ex ea commodo consequat.</p>
      <p class="body">Excepteur sint occaecat cupidatat non proident, sunt in culpa qui officia deserunt mollit anim id est laborum. re et dolore magnam aliquam quaerat voluptatem.</p>
      <p class="signoff">Regards</p>
      <div class="signature" role="img" aria-label="Handwritten signature of Daniel Hart"></div>
    </article>
    <svg class="footer-bands" viewBox="0 0 540 60" preserveAspectRatio="none" aria-hidden="true">
      <polygon points="0,22 200,22 230,60 0,60" fill="var(--charcoal)"/>
      <polygon points="205,22 540,22 540,60 235,60" fill="#fff"/>
      <polygon points="212,30 540,30 540,60 238,60" fill="var(--green)"/>
    </svg>
  </main>
</body>
</html>
```